Skin Care Product Line needs custom designed labels

We need one to two label design templates that can be used across our natural skin care products such as body lotion, salt scrubs, lip balms, handmade soaps, body creams, body mists, foot creams, bath salts. The design will come in different colors. We have our own logo; however the logo should have the flower colored golden along with the word tisbel.
Label sizes are :
1) 6 inches by 4 inches rectangular for body lotion,
2) 81/2 inches by 2 inches rectangular for body scrub,
3) 5 inches by 3 inches rectangular for body mist,
4) 2 inches by 3 inches for bath salts,
5) 2.125 inches by 2.125 inches for lip balm,
6) 11/2 inches by 1/12 inches label for soap.

The design should have a beige background with one color or two of the same colors for instance light lavender and a darker lavender. It should have a vintage feel to it because it's for a natural skin care line not commercial type. Also the fonts should be vintage looking. We can have one design with different colors such as light green, light yellow, light pink, light blue , light orange to go with the different scents. Added Tuesday, January 26, 2016

Target Market(s)

Young adults and aging boomers

Industry/Entity Type

Skin Care Product

Font styles to use
Decorative

Colors
cfeae6
b7a5cd
e4daeb
fbf289
fac994
9bcb3b
f9d9e8
f04a50
f68d4c

Requirements
Must have
• Please see attached image for design sample. Original Label design should have beige to tan colored background similar to the attached file. light colors such as lavender, light yellow, light orange, etc can be changed once original label is designed. We would need to be able to edit label design text and label design colors to match our different scents after we decide on the design.

```html
<!DOCTYPE html>
<html lang="en">
<head>
<meta charset="utf-8">
<title>Velora Tisbel – Jojoba Facial Moisturizer Labels</title>
<link rel="stylesheet" href="https://fonts.googleapis.com/css2?family=Cormorant+Garamond:wght@500&family=Pinyon+Script&display=swap">
<style>
  :root {
    --page: #efe6e6;
    --lavender-paper: #f4eff3;
    --beige-paper: #eeedd9;
    --ink: #3a3a3a;
    --ink-soft: #6b6b6b;
    --brand-olive: #7d7a3c;
    --ornament: #b9b6b4;
    --plate-lavender: #ebe5ea;
    --plate-beige: #e2e1c6;
  }
  * { box-sizing: border-box; margin: 0; padding: 0; }
  html, body { width: 1200px; height: 640px; overflow: hidden; }
  body {
    background: var(--page);
    font-family: "Cormorant Garamond", Georgia, serif;
    color: var(--ink);
  }
  .label-row {
    position: absolute;
    left: 70px; top: 150px;
    display: flex;
    gap: 60px;
  }
  .label {
    position: relative;
    width: 220px; height: 340px;
    box-shadow: 0 2px 6px rgba(0,0,0,0.12);
  }
  .label--lavender { background: var(--lavender-paper); }
  .label--beige { background: var(--beige-paper); }
  .label__frame {
    position: absolute; inset: 8px;
    border: 1.5px solid var(--ink);
  }
  .label__frame::after {
    content: ""; position: absolute; inset: 4px;
    border: 0.75px solid var(--ink-soft);
  }
  .corner {
    position: absolute; width: 38px; height: 38px;
    background: var(--ornament); opacity: 0.7;
  }
  .corner--tl { top: 14px; left: 14px; }
  .corner--tr { top: 14px; right: 14px; }
  .corner--bl { bottom: 14px; left: 14px; }
  .corner--br { bottom: 14px; right: 14px; }
  .brand {
    position: absolute; top: 46px; left: 0; right: 0;
    text-align: center;
  }
  .brand__name {
    font-family: "Cormorant Garamond", Georgia, serif;
    font-weight: 500; font-size: 19px;
    color: var(--brand-olive);
  }
  .brand__tagline {
    font-size: 7px; color: var(--ink-soft); letter-spacing: 0.5px;
  }
  .product {
    position: absolute; top: 140px; left: 0; right: 0;
    text-align: center;
  }
  .product__plate {
    margin: 0 auto; width: 140px; padding: 8px 0 6px;
    border: 1px solid var(--ink); border-radius: 10px;
  }
  .label--lavender .product__plate { background: var(--plate-lavender); }
  .label--beige .product__plate { background: var(--plate-beige); }
  .product__name {
    font-family: "Pinyon Script", cursive;
    font-size: 24px; line-height: 1.1;
  }
  .product__type {
    font-family: "Pinyon Script", cursive;
    font-size: 12px; color: var(--ink-soft);
  }
  .divider {
    margin: 14px auto 0; width: 90px; height: 12px;
    background: var(--ornament); opacity: 0.7; border-radius: 6px;
  }
  .line-note {
    position: absolute; bottom: 36px; left: 0; right: 0;
    text-align: center;
    font-family: "Pinyon Script", cursive; font-size: 15px;
  }
</style>
</head>
<body>
<main class="label-row">

  <section class="label label--lavender">
    <div class="label__frame"></div>
    <div class="corner corner--tl" role="img" aria-label="Vintage corner flourish"></div>
    <div class="corner corner--tr" role="img" aria-label="Vintage corner flourish"></div>
    <div class="corner corner--bl" role="img" aria-label="Vintage corner flourish"></div>
    <div class="corner corner--br" role="img" aria-label="Vintage corner flourish"></div>
    <header class="brand">
      <div class="brand__name">Velora Tisbel</div>
      <div class="brand__tagline">Pure Natural Skin Care</div>
    </header>
    <div class="product">
      <div class="product__plate">
        <div class="product__name">Jojoba Facial</div>
        <div class="product__type">Moisturizer</div>
      </div>
    </div>
    <div class="line-note">Natural Products</div>
  </section>

  <section class="label label--lavender">
    <div class="label__frame"></div>
    <div class="corner corner--tl" role="img" aria-label="Vintage corner flourish"></div>
    <div class="corner corner--tr" role="img" aria-label="Vintage corner flourish"></div>
    <div class="corner corner--bl" role="img" aria-label="Vintage corner flourish"></div>
    <div class="corner corner--br" role="img" aria-label="Vintage corner flourish"></div>
    <header class="brand">
      <div class="brand__name">Velora Tisbel</div>
      <div class="brand__tagline">Pure Natural Skin Care</div>
    </header>
    <div class="product">
      <div class="product__name">Jojoba Facial</div>
      <div class="product__type">Moisturizer</div>
      <div class="divider" role="img" aria-label="Scrolled divider ornament"></div>
    </div>
    <div class="line-note">Natural Products</div>
  </section>

  <section class="label label--beige">
    <div class="label__frame"></div>
    <div class="corner corner--tl" role="img" aria-label="Vintage corner flourish"></div>
    <div class="corner corner--tr" role="img" aria-label="Vintage corner flourish"></div>
    <div class="corner corner--bl" role="img" aria-label="Vintage corner flourish"></div>
    <div class="corner corner--br" role="img" aria-label="Vintage corner flourish"></div>
    <header class="brand">
      <div class="brand__name">Velora Tisbel</div>
      <div class="brand__tagline">Pure Natural Skin Care</div>
    </header>
    <div class="product">
      <div class="product__name">Jojoba Facial</div>
      <div class="product__type">Moisturizer</div>
      <div class="divider" role="img" aria-label="Scrolled divider ornament"></div>
    </div>
    <div class="line-note">Natural Products</div>
  </section>

  <section class="label label--beige">
    <div class="label__frame"></div>
    <div class="corner corner--tl" role="img" aria-label="Vintage corner flourish"></div>
    <div class="corner corner--tr" role="img" aria-label="Vintage corner flourish"></div>
    <div class="corner corner--bl" role="img" aria-label="Vintage corner flourish"></div>
    <div class="corner corner--br" role="img" aria-label="Vintage corner flourish"></div>
    <header class="brand">
      <div class="brand__name">Velora Tisbel</div>
      <div class="brand__tagline">Pure Natural Skin Care</div>
    </header>
    <div class="product">
      <div class="product__plate">
        <div class="product__name">Jojoba Facial</div>
        <div class="product__type">Moisturizer</div>
      </div>
    </div>
    <div class="line-note">Natural Products</div>
  </section>

</main>
</body>
</html>
```